Debut book club fiction author needs a book cover design

I need a book cover design (and a separate e-book thumbnail also) for my book club/women's fiction debut that I am launching on Brightleaf Press Portal. I've included the brief/back cover blurb as below to give you a flavour of the book. I'm after something striking but simple, maybe with a wine glass lurking in the background and/or an abandoned dummy/pacifier or empty crib?? I've attached a few competitor style covers that i like for reference.

Target Market(s)

Women's fiction readers

Industry/Entity Type

Women's fiction/publishing

Font styles to use
Serif

Requirements
Must have
• Title: Every Quiet Hour. Name: Maren Tolley. The full 'pitch/blurb' on the back cover which I've included as a file below named 'pitch'
Nice to have
• Open to suggestions, but an image which reflects the struggle captured in the book in a bold simple image

```html
<!DOCTYPE html>
<html lang="en">
<head>
<meta charset="utf-8">
<title>Every Quiet Hour — Maren Tolley</title>
<link rel="stylesheet" href="https://fonts.googleapis.com/css2?family=Cinzel:wght@400;700;900&display=swap">
<style>
  :root {
    --page: #ffffff;
    --cover-black: #000000;
    --accent-red: #f20000;
    --glow-red: #b00006;
    --title-white: #ffffff;
  }
  html, body {
    margin: 0;
    padding: 0;
    width: 1200px;
    height: 1200px;
    overflow: hidden;
    background: var(--page);
  }
  .canvas {
    position: relative;
    width: 1200px;
    height: 1200px;
  }
  .book-cover {
    position: absolute;
    left: 293px;
    top: 140px;
    width: 614px;
    height: 920px;
    display: block;
  }
  .title-line {
    font-family: 'Cinzel', serif;
    text-anchor: middle;
  }
  .title-line--light { fill: var(--title-white); font-weight: 400; font-size: 134px; }
  .title-line--accent { fill: var(--accent-red); font-weight: 900; font-size: 158px; }
  .title-line--heavy { fill: var(--title-white); font-weight: 900; font-size: 134px; }
  .author-name {
    font-family: 'Cinzel', serif;
    font-weight: 700;
    font-size: 27px;
    fill: var(--title-white);
    text-anchor: middle;
    letter-spacing: 1px;
  }
  .author-band { fill: var(--accent-red); }
  .cover-ground { fill: var(--cover-black); }
</style>
</head>
<body>
<main class="canvas">
  <svg class="book-cover" viewBox="0 0 614 920" xmlns="http://www.w3.org/2000/svg">
    <defs>
      <radialGradient id="glass-glow" cx="0.5" cy="0.52" r="0.42" fx="0.5" fy="0.6">
        <stop offset="0" stop-color="var(--glow-red)"/>
        <stop offset="0.35" stop-color="#5a0003"/>
        <stop offset="1" stop-color="var(--cover-black)"/>
      </radialGradient>
    </defs>

    <rect class="cover-ground" x="0" y="0" width="614" height="920"/>

    <rect class="cover-photo" x="0" y="0" width="614" height="470" fill="url(#glass-glow)"
          role="img" aria-label="Photograph of red wine being poured from a dark bottle into a stemmed wine glass, lit by a red glow against black"/>

    <text class="title-line title-line--light" x="307" y="598" textLength="532" lengthAdjust="spacingAndGlyphs">EVERY</text>
    <text class="title-line title-line--accent" x="307" y="726" textLength="532" lengthAdjust="spacingAndGlyphs">QUIET</text>
    <text class="title-line title-line--heavy" x="307" y="841" textLength="532" lengthAdjust="spacingAndGlyphs">HOUR</text>

    <rect class="author-band" x="0" y="872" width="614" height="48"/>
    <text class="author-name" x="307" y="906">MAREN TOLLEY</text>
  </svg>
</main>
</body>
</html>
```